Letterhead and Envelopes design using existing logo. Logo can be found at ridgemontcaldera.com

Use existing logo (attached) and incorporate in letterhead and envelope designs.

Current logo can be viewed at ridgemontcaldera.com the web site reflect various parent and sub companies. Please see attached as well.

Target Market(s)

Other oil and gas operators.

Industry/Entity Type

Oil And Gas

Font styles to use
Sans Serif

Colors

Designer to choose colors to be used in the design.

Requirements
Must have
• Current logo and address
Nice to have
• Modern, contemporary approach yet incorporate existing traditional design.
• After design is selected for Ridgemont Caldera Holdings I will use similar design for Royalties, Exploration, Energy and Farms with different color schemes.

```html
<!DOCTYPE html>
<html lang="en">
<head>
<meta charset="utf-8">
<title>Ridgemont Caldera Holdings – Stationery Option 03</title>
<link href="https://fonts.googleapis.com/css2?family=Arimo:wght@400;700&family=Source+Sans+3:wght@300&display=swap" rel="stylesheet">
<style>
  :root {
    --brand-green: #6f9a3e;
    --ink: #111111;
    --label-grey: #e4e4e4;
    --paper: #ffffff;
    --flap-grey: #f2f2f4;
    --edge: #e2e2e2;
    --mark-grey: #ececec;
  }
  * { box-sizing: border-box; margin: 0; padding: 0; }
  html, body { width: 1200px; height: 1200px; overflow: hidden; background: var(--paper); }
  body { position: relative; font-family: "Arimo", Arial, sans-serif; color: var(--ink); }

  .section-label {
    position: absolute;
    font-family: "Source Sans 3", "Myriad Pro", sans-serif;
    font-weight: 300;
    color: var(--label-grey);
    line-height: 1;
    white-space: nowrap;
  }
  .option-title { left: 78px; top: 90px; font-size: 70px; }
  .letterhead-label { left: 77px; top: 272px; font-size: 35px; }
  .envelope-label { left: 853px; top: 443px; font-size: 35px; }

  .sheet {
    position: absolute;
    background: var(--paper);
    border: 1px solid var(--edge);
    overflow: hidden;
  }
  .letterhead { left: 80px; top: 324px; width: 571px; height: 808px; }
  .envelope { left: 687px; top: 538px; width: 482px; height: 316px; border-radius: 40px 40px 0 0; }

  .faint-mark {
    position: absolute;
    border-radius: 50%;
    border: 6px solid var(--mark-grey);
  }
  .letterhead .faint-mark { left: 254px; top: 40px; width: 320px; height: 320px; }
  .envelope .faint-mark { left: 331px; top: 98px; width: 152px; height: 152px; border-width: 4px; }

  .flap { position: absolute; left: 0; top: 0; width: 100%; height: 79px; background: var(--flap-grey); }

  .brand-band { position: absolute; left: 0; width: 100%; background: var(--brand-green); }
  .letterhead .brand-band { top: 0; height: 81px; }
  .envelope .brand-band { top: 79px; height: 39px; }

  .brand-dot {
    position: absolute;
    border-radius: 50%;
    background: var(--paper);
  }
  .letterhead .brand-dot { left: 35px; top: 34px; width: 88px; height: 88px; }
  .envelope .brand-dot { left: 19px; top: 83px; width: 64px; height: 64px; }

  .brand-name {
    position: absolute;
    color: var(--paper);
    font-weight: 700;
    white-space: nowrap;
    line-height: 1;
  }
  .letterhead .brand-name { left: 138px; top: 56px; font-size: 21px; }
  .envelope .brand-name { left: 99px; top: 98px; font-size: 17px; }

  .address-window {
    position: absolute;
    left: 14px; top: 180px; width: 172px; height: 60px;
    border: 1px solid var(--edge);
  }

  .sender { position: absolute; line-height: 1; white-space: nowrap; }
  .sender-name { font-size: 13.5px; font-weight: 700; letter-spacing: -0.1px; }
  .sender-address { font-size: 8.6px; margin-top: 5px; }
  .letterhead .sender { left: 41px; top: 742px; }
  .envelope .sender { left: 14px; top: 274px; }

  .contact-tab {
    position: absolute;
    width: 197px; height: 42px;
    background: var(--brand-green);
    border-radius: 8px 0 0 8px;
    color: var(--paper);
    font-size: 9px;
    line-height: 12px;
    padding: 7px 0 0 10px;
    white-space: nowrap;
  }
  .contact-tab strong { font-weight: 700; }
  .letterhead .contact-tab { left: 374px; top: 724px; }
  .envelope .contact-tab { left: 285px; top: 263px; height: 41px; }
</style>
</head>
<body>
  <div class="section-label option-title">OPTION 03</div>
  <div class="section-label letterhead-label">LETTERHEAD</div>
  <div class="section-label envelope-label">ENVELOPE</div>

  <section class="sheet letterhead" aria-label="Letterhead">
    <div class="faint-mark"></div>
    <div class="brand-band"></div>
    <div class="brand-dot"></div>
    <div class="brand-name">RIDGEMONT CALDERA HOLDINGS</div>
    <div class="sender">
      <div class="sender-name">Ridgemont Caldera Holdings, LLC.</div>
      <div class="sender-address">PO Box 318 Harlow, Montana 59036</div>
    </div>
    <div class="contact-tab">
      Website: <strong>www.ridgemontcaldera.com</strong><br>
      E-mail : reception@ridgemontcaldera.com
    </div>
  </section>

  <section class="sheet envelope" aria-label="Envelope">
    <div class="flap"></div>
    <div class="faint-mark"></div>
    <div class="brand-band"></div>
    <div class="brand-dot"></div>
    <div class="brand-name">RIDGEMONT CALDERA HOLDINGS</div>
    <div class="address-window"></div>
    <div class="sender">
      <div class="sender-name">Ridgemont Caldera Holdings, LLC.</div>
      <div class="sender-address">PO Box 318 Harlow, Montana 59036</div>
    </div>
    <div class="contact-tab">
      Website: <strong>www.ridgemontcaldera.com</strong><br>
      E-mail : reception@ridgemontcaldera.com
    </div>
  </section>
</body>
</html>
```